Letterhead for small civil engineer company

We need bold and modern design for company letterhead in MS word. It needs to have company logo and company info. Somewhere in the upper right part of document needs to be space for "recever" and the documents starts with, example, "SUBJECT: CIVIL ENGINEER LETTERHEAD".

in the bottom part of document needs to be signature and date.

Company info: Veltrana d.o.o., Lipovac 15, Lipovac (Općina Brdarić), OIB 47396028154, www.veltrana.hr, info@veltrana.hr

Email of document sender needs to be somewhere if document, exapmle xyz@veltrana.hr

Target Market(s)

Civil engineer company and projects

Industry/Entity Type

Civil engineer

Font styles to use
Serif

Colors
F0912C
F2A743
F7CA91
FBE8D2
FDF5EE

Requirements
Must have
• Company logo and company info
Nice to have
• Moder and clean design
Should not have
• Too much details

```html
<!DOCTYPE html>
<html lang="en">
<head>
<meta charset="utf-8">
<title>Veltrana d.o.o. – Letterhead</title>
<link rel="stylesheet" href="https://fonts.googleapis.com/css2?family=Space+Grotesk:wght@400;500;700&display=swap">
<style>
  :root {
    --backdrop: #b3b3b3;
    --paper: #ffffff;
    --panel: #efefef;
    --accent: #e8781f;
    --accent-soft: #fbf1e8;
    --ink: #1e1e1e;
    --ink-muted: #555555;
    --rule: #8a8a8a;
  }
  * { margin: 0; padding: 0; box-sizing: border-box; }
  html, body {
    width: 1200px; height: 1000px; overflow: hidden;
    background: var(--backdrop);
    font-family: "Space Grotesk", sans-serif;
    color: var(--ink);
  }
  .letterhead {
    position: absolute; left: 297px; top: 72px;
    width: 606px; height: 856px;
    background: var(--paper);
    box-shadow: 0 1px 4px rgba(0,0,0,0.25);
    overflow: hidden;
  }
  .letterhead__backdrop { position: absolute; inset: 0; }
  .abs { position: absolute; }

  .brand { left: 33px; top: 38px; display: flex; align-items: center; gap: 8px; }
  .brand__square { width: 34px; height: 34px; border: 1px solid var(--ink-muted); }
  .brand__name { font-size: 23px; font-weight: 500; color: var(--accent); letter-spacing: 0.5px; }

  .receiver { right: 62px; top: 47px; font-size: 11px; }

  .sender { left: 34px; top: 86px; font-size: 11px; line-height: 14px; }
  .subject { left: 34px; top: 127px; font-size: 11px; line-height: 15px; }
  .subject__label { font-weight: 700; }

  .sign-field { left: 76px; width: 196px; text-align: center; font-size: 9.5px; color: var(--ink-muted); }
  .sign-field__line { border-top: 1px solid var(--rule); height: 0; margin-bottom: 6px; position: relative; }
  .sign-field--signature { top: 733px; }
  .sign-field--date { top: 798px; }
  .date-slash { position: absolute; top: -14px; font-size: 10px; color: var(--ink-muted); }

  .company { right: 62px; top: 697px; text-align: right; font-size: 11.5px; line-height: 14.6px; color: var(--ink-muted); }
  .company__name { font-weight: 700; color: #333; margin-bottom: 15px; }
  .company__address { margin-bottom: 15px; }
  .company__web-name { color: var(--accent); font-weight: 700; }
</style>
</head>
<body>
<main class="letterhead">
  <svg class="letterhead__backdrop" width="606" height="856" viewBox="0 0 606 856" aria-hidden="true">
    <polygon points="0,0 148,0 56,856 0,856" fill="var(--panel)"/>
    <polygon points="606,560 606,690 470,856 330,856" fill="var(--accent-soft)"/>
  </svg>

  <div class="brand abs">
    <span class="brand__square"></span>
    <span class="brand__name">VELTRANA</span>
  </div>

  <p class="receiver abs">recever</p>

  <div class="sender abs">
    <p>sender</p>
    <p>xyz@veltrana.hr</p>
  </div>

  <div class="subject abs">
    <p class="subject__label">SUBJECT:</p>
    <p>CIVIL ENGINEER LETTERHEAD</p>
  </div>

  <div class="sign-field sign-field--signature abs">
    <div class="sign-field__line"></div>
    <p>Signature</p>
  </div>

  <div class="sign-field sign-field--date abs">
    <div class="sign-field__line">
      <span class="date-slash" style="left:72px">/</span>
      <span class="date-slash" style="left:121px">/</span>
    </div>
    <p>Date</p>
  </div>

  <address class="company abs" style="font-style:normal">
    <p class="company__name">VELTRANA D.O.O.</p>
    <div class="company__address">
      <p>LIPOVAC 15</p>
      <p>LIPOVAC (OPĆINA BRDARIĆ)</p>
      <p>OIB 47396028154</p>
    </div>
    <p>info@veltrana.hr</p>
    <p><span class="company__web-name">veltrana</span>.hr</p>
  </address>
</main>
</body>
</html>
```